Postcard Design

Law office.
Details are on the attached pdf file:
NOTE: the following items are to be changed, as follows:
1. price is 799
2. delete "Expires 2-8-13"
3. make "Nevada County's..." into "Northern California's ... "
4. Someplace where it fits nicely, add "Fast, Easy, Done!"
5. Delete "no obligation first visit"
6. That attached pdf was a successful ad so I want to maintain that look GENERALLY, but I'm not stuck on anything in particular. Some freedom to play with it for a perfect ad.
7. I'll attach the revised picture and the logo.

```html
<!DOCTYPE html>
<html lang="en">
<head>
<meta charset="utf-8">
<title>Law Office Postcard</title>
<link href="https://fonts.googleapis.com/css2?family=Crimson+Text:ital@1&family=Montserrat:wght@500;700&family=Oswald:wght@500&family=Pinyon+Script&family=Roboto+Condensed:ital,wght@0,400;0,700;1,400;1,700&display=swap" rel="stylesheet">
<style>
  :root {
    --page: #e9e6e1;
    --white: #ffffff;
    --panel: #2b2523;
    --band: #3a4634;
    --seal: #4f5a38;
    --seal-line: #c9c99a;
    --gold: #efe6a8;
    --cream: #f2eeb6;
    --yellow: #f5e33a;
    --price: #f7ee8a;
    --ink: #1f1d1c;
    --web: #2d3a2a;
  }
  html, body {
    margin: 0;
    width: 1200px;
    height: 1000px;
    overflow: hidden;
    background: var(--page);
  }
  .postcard {
    position: absolute;
    left: 67px;
    top: 115px;
    width: 1066px;
    height: 770px;
    background: var(--white);
    overflow: hidden;
  }
  .portrait {
    position: absolute;
    left: 0;
    top: 0;
    width: 720px;
    height: 600px;
    background: radial-gradient(ellipse at 42% 40%, #aebac2 0%, #8f9ea8 45%, #6f7d86 100%);
  }
  .shapes {
    position: absolute;
    inset: 0;
  }
  .t {
    position: absolute;
    transform: translate(-50%, -50%);
    white-space: nowrap;
    margin: 0;
    line-height: 1;
  }
  .brand-name {
    left: 767px; top: 86px;
    font: 700 22px "Roboto Condensed", sans-serif;
    color: var(--ink);
  }
  .tagline {
    left: 943px; top: 122px;
    font: italic 26px/1.2 "Crimson Text", serif;
    color: var(--ink);
    text-align: center;
  }
  .office-label {
    left: 826px; top: 233px;
    font: 700 25px "Roboto Condensed", sans-serif;
    color: var(--white);
  }
  .attorney-name {
    left: 828px; top: 292px;
    font: 56px "Pinyon Script", cursive;
    color: var(--gold);
  }
  .headline {
    left: 830px; top: 377px;
    font: 700 34px/1.3 "Roboto Condensed", sans-serif;
    color: var(--white);
    text-align: center;
  }
  .services {
    left: 830px; top: 442px;
    font: italic 19px "Crimson Text", serif;
    color: var(--white);
  }
  .protect {
    left: 835px; top: 515px;
    font: 400 34px "Roboto Condensed", sans-serif;
    color: var(--cream);
  }
  .call-line {
    left: 835px; top: 557px;
    font: 500 24px "Montserrat", sans-serif;
    color: var(--white);
  }
  .call-line strong { color: var(--yellow); font-weight: 700; }
  .price {
    left: 503px; top: 535px;
    font: 500 84px "Oswald", sans-serif;
    color: var(--price);
  }
  .value {
    left: 503px; top: 605px;
    font: 400 21px "Roboto Condensed", sans-serif;
    color: var(--price);
  }
  .notary {
    left: 233px; top: 646px;
    font: italic 700 31px "Roboto Condensed", sans-serif;
    color: var(--white);
  }
  .slogan {
    left: 233px; top: 714px;
    font: italic 700 42px "Roboto Condensed", sans-serif;
    color: var(--white);
  }
  .phone {
    left: 665px; top: 648px;
    transform: translate(0, -50%);
    font: 700 44px "Montserrat", sans-serif;
    color: var(--ink);
  }
  .check-label {
    left: 810px; top: 692px;
    font: italic 20px "Crimson Text", serif;
    color: var(--ink);
  }
  .website {
    left: 810px; top: 726px;
    font: 700 28px "Montserrat", sans-serif;
    color: var(--web);
  }
</style>
</head>
<body>
<main class="postcard">
  <div class="portrait" role="img" aria-label="Portrait photo of the attorney in a dark suit and tie, smiling, against a grey studio backdrop"></div>

  <svg class="shapes" viewBox="0 0 1066 770" width="1066" height="770" aria-hidden="true">
    <path d="M703 0 L1066 0 L1066 172 L611 172 C628 90 655 28 703 0 Z" fill="var(--white)"/>
    <path d="M611 172 L1066 172 L1066 598 L538 598 C555 430 585 270 611 172 Z" fill="var(--panel)"/>
    <path d="M0 598 L1066 598 L1066 770 L0 770 Z" fill="var(--white)"/>
    <path d="M0 598 L498 598 L536 770 L0 770 Z" fill="var(--band)"/>
    <line x1="616" y1="325" x2="1043" y2="325" stroke="var(--white)" stroke-width="1.2" stroke-dasharray="3 3"/>
    <line x1="640" y1="475" x2="1020" y2="475" stroke="#5a4f4b" stroke-width="1"/>
    <line x1="108" y1="677" x2="373" y2="677" stroke="#7f8a66" stroke-width="1.5"/>
    <circle cx="503" cy="557" r="118" fill="var(--seal)" stroke="var(--white)" stroke-width="3"/>
    <circle cx="503" cy="557" r="109" fill="none" stroke="var(--seal-line)" stroke-width="1.5"/>
    <g class="phone-icon">
      <rect x="605" y="631" width="50" height="34" rx="5" fill="var(--band)"/>
      <path d="M613 646 Q630 633 647 646 L643 651 L636 648 L636 644 Q630 642 624 644 L624 648 L617 651 Z" fill="var(--white)"/>
      <rect x="620" y="652" width="20" height="8" rx="1.5" fill="var(--white)"/>
    </g>
  </svg>

  <p class="t brand-name">Moreno Law</p>
  <p class="t tagline">Thousands Served<br>Since 1998</p>

  <p class="t office-label">THE LAW OFFICE OF</p>
  <p class="t attorney-name">Daniel R. Moreno</p>
  <h1 class="t headline">Northern California’s Best in<br>Estate Plans</h1>
  <p class="t services">Living Trusts, Wills &amp; All Necessary Documents</p>
  <p class="t protect">Protect Your Loved Ones!</p>
  <p class="t call-line">It’s Easy - <strong>CALL NOW!</strong></p>

  <p class="t price">$799</p>
  <p class="t value">Over $2,000 value</p>

  <p class="t notary">Free Notarization</p>
  <p class="t slogan">Fast, Easy, Done!</p>

  <p class="t phone">(530)-555-0142</p>
  <p class="t check-label">Check me out at</p>
  <p class="t website">www.danielmorenolaw.com</p>
</main>
</body>
</html>
```